I need creative and unique business card design using my company logo. Ok to change logo color. We are a small brokerage doing both Real Estate and Mortgage services. Need to have the follow on business card;
1. agent name - Nora Velden - Realtor
2. cell - 949-555-0182
3. license number - DRE 07164392
4. business name - Bright Keys & Lending, Inc
5. business office - 626-555-0147
6. business address - 214 W. Marlowe Ave #308, Arcadia CA 91006
7. business logo - attached (ok to use different color on logo)

```html
<!DOCTYPE html>
<html lang="en">
<head>
<meta charset="utf-8">
<title>Bright Keys &amp; Lending – Business Card</title>
<link href="https://fonts.googleapis.com/css2?family=Arimo:wght@400;700&display=swap" rel="stylesheet">
<style>
  :root {
    --bg: #e4e6ea;
    --card: #ffffff;
    --blue-deep: #2455a8;
    --blue-light: #4aa3dc;
    --grey-wave: #a6a6a6;
    --ink: #333333;
  }
  * { margin: 0; padding: 0; box-sizing: border-box; }
  html, body { width: 1200px; height: 903px; overflow: hidden; }
  body {
    background: var(--bg);
    font-family: "Arimo", Arial, sans-serif;
    position: relative;
  }
  .card {
    position: absolute;
    width: 540px;
    height: 309px;
    background: var(--card);
    box-shadow: 0 6px 18px rgba(0,0,0,.18);
    overflow: hidden;
  }
  .card--front { left: 45px; top: 297px; }
  .card--back { left: 615px; top: 297px; }

  .wave { position: absolute; left: 0; top: 0; width: 100%; height: 100%; }

  .brand {
    position: absolute;
    display: flex;
    align-items: center;
    gap: 10px;
  }
  .brand__square {
    width: 34px; height: 34px;
    background: var(--blue-deep);
    flex: none;
  }
  .brand__name {
    color: var(--blue-deep);
    font-weight: 400;
    font-size: 15px;
    letter-spacing: 1.5px;
    text-transform: uppercase;
    line-height: 1.25;
  }
  .card--front .brand { left: 32px; top: 70px; width: 220px; }
  .card--back .brand { left: 0; right: 0; top: 130px; justify-content: center; }
  .card--back .brand__square { width: 44px; height: 44px; }
  .card--back .brand__name { font-size: 19px; letter-spacing: 2px; }

  .divider {
    position: absolute;
    left: 268px; top: 58px;
    width: 1.5px; height: 152px;
    background: var(--blue-deep);
  }

  .contact {
    position: absolute;
    left: 286px; top: 54px;
    color: var(--ink);
    font-size: 13.5px;
    line-height: 1.28;
  }
  .contact__name {
    font-weight: 700;
    font-size: 21px;
    text-transform: uppercase;
    margin-bottom: 2px;
  }
  .contact__first { color: var(--blue-deep); }
  .contact__last { color: var(--blue-light); }
  .contact__line { display: flex; align-items: center; gap: 5px; }
  .icon { width: 11px; height: 11px; fill: var(--blue-deep); flex: none; }
</style>
</head>
<body>

<section class="card card--front" aria-label="Business card front">
  <svg class="wave" viewBox="0 0 540 309" preserveAspectRatio="none" aria-hidden="true">
    <defs>
      <linearGradient id="waveBlue" x1="0" y1="0" x2="1" y2="0">
        <stop offset="0" stop-color="#2455a8"/>
        <stop offset="0.55" stop-color="#4aa3dc"/>
        <stop offset="1" stop-color="#2a5bb0"/>
      </linearGradient>
    </defs>
    <path d="M0 118 C 140 150, 200 300, 540 268 L540 309 L0 309 Z" fill="var(--grey-wave)"/>
    <path d="M0 128 C 140 165, 200 306, 540 278 L540 309 L0 309 Z" fill="#ffffff"/>
    <path d="M0 140 C 140 185, 210 318, 540 290 L540 309 L0 309 Z" fill="url(#waveBlue)"/>
  </svg>

  <div class="brand">
    <span class="brand__square"></span>
    <span class="brand__name">Bright Keys &amp; Lending, Inc</span>
  </div>

  <div class="divider"></div>

  <div class="contact">
    <p class="contact__name"><span class="contact__first">Nora</span> <span class="contact__last">Velden</span></p>
    <p>Realtor</p>
    <p>Bright Keys &amp; Lending, Inc</p>
    <p>214 W. Marlowe Ave</p>
    <p>#308, Arcadia CA 91006</p>
    <p class="contact__line">
      <svg class="icon" viewBox="0 0 24 24" aria-hidden="true"><path d="M7 2h10a2 2 0 0 1 2 2v16a2 2 0 0 1-2 2H7a2 2 0 0 1-2-2V4a2 2 0 0 1 2-2zm0 3v13h10V5z"/></svg>
      949-555-0182
    </p>
    <p class="contact__line">
      <svg class="icon" viewBox="0 0 24 24" aria-hidden="true"><path d="M6.6 10.8a15.1 15.1 0 0 0 6.6 6.6l2.2-2.2a1 1 0 0 1 1-.25 11.4 11.4 0 0 0 3.6.57 1 1 0 0 1 1 1V20a1 1 0 0 1-1 1A17 17 0 0 1 3 4a1 1 0 0 1 1-1h3.5a1 1 0 0 1 1 1c0 1.25.2 2.45.57 3.57a1 1 0 0 1-.25 1z"/></svg>
      626-555-0147
    </p>
    <p>DRE 07164392</p>
  </div>
</section>

<section class="card card--back" aria-label="Business card back">
  <div class="brand">
    <span class="brand__square"></span>
    <span class="brand__name">Bright Keys &amp; Lending, Inc</span>
  </div>
</section>

</body>
</html>
```